Packaging design for a low carb bar

I am producing a low carb / high fat bar, therefore I would like to have a light weighted modern design. The background color pastel light or something like that. The package should be focused on fitness-active individuals who are looking for healthy low carb snacks. Preliminary packaging size, logo, and more details on what should be attached to the packaging are attached. Thank you!

```html
<!DOCTYPE html>
<html lang="en">
<head>
<meta charset="utf-8">
<title>Keto Bar – Almond Flavour packaging</title>
<link rel="stylesheet" href="https://fonts.googleapis.com/css2?family=Oswald:wght@300;400&family=Montserrat:wght@500;600;700&family=Cormorant+SC:wght@600&display=swap">
<style>
  :root {
    --backdrop: #d39ac9;
    --sky-top: #a9d6e8;
    --sky: #6db6d4;
    --sky-soft: #8cc7df;
    --white: #ffffff;
    --paper: #e9e9ec;
    --teal: #3f97a3;
    --teal-deep: #2f7f8c;
    --logo: #4ea9b2;
    --plum: #8b4f98;
    --check: #b455a6;
  }
  * { box-sizing: border-box; margin: 0; padding: 0; }
  html, body { width: 1200px; height: 1200px; overflow: hidden; }
  body { background: var(--backdrop); position: relative; font-family: "Montserrat", sans-serif; }

  .pack {
    position: absolute; left: 320px; top: 60px;
    width: 560px; height: 1080px;
    background: var(--sky);
    overflow: hidden;
  }
  .pack__top { position: absolute; left: 0; top: 0; width: 100%; height: 100px; background: var(--sky-top); }
  .pack__stripe { position: absolute; left: 0; top: 100px; width: 100%; height: 46px; background: var(--white); }

  .brand {
    position: absolute; left: 330px; top: 34px;
    width: 176px; height: 176px; border-radius: 50%;
    background: var(--logo);
    display: flex; align-items: center; justify-content: center;
  }
  .brand__name {
    font-family: "Oswald", sans-serif; font-weight: 300;
    color: var(--white); font-size: 30px; letter-spacing: 3px;
    text-align: center; line-height: 1.05; text-transform: uppercase;
  }

  .title {
    position: absolute; left: 150px; top: 250px;
    width: 290px; height: 300px;
    border: 2px solid rgba(255,255,255,.75);
    display: flex; flex-direction: column; align-items: center; justify-content: center;
  }
  .title__line {
    font-family: "Oswald", sans-serif; font-weight: 400;
    color: var(--white); line-height: .9; letter-spacing: 2px;
    text-shadow: 4px 4px 0 var(--teal-deep);
  }
  .title__line--keto { font-size: 128px; }
  .title__line--bar { font-size: 150px; }

  .claims {
    position: absolute; left: 118px; top: 590px;
    list-style: none; color: var(--white);
    font-size: 17px; font-weight: 600; letter-spacing: .5px; text-transform: uppercase;
  }
  .claims li { display: flex; align-items: center; gap: 10px; margin-bottom: 8px; }
  .claims svg { flex: none; }

  .wave { position: absolute; left: 0; top: 640px; width: 560px; height: 440px; }

  .ingredients {
    position: absolute; left: 0; top: 780px; width: 560px; height: 220px;
  }
  .ingredients__label {
    position: absolute; left: 50%; top: 0; transform: translateX(-50%);
    background: var(--paper); padding: 0 12px;
    color: var(--teal); font-weight: 700; font-size: 20px; letter-spacing: 1px;
  }
  .ingredients__band {
    position: absolute; left: 0; top: 100px; width: 100%; height: 48px; background: var(--teal);
  }
  .ingredients__row {
    position: absolute; left: 14px; top: 42px; width: 532px;
    display: flex; list-style: none;
  }
  .ingredient {
    flex: 1; display: flex; flex-direction: column; align-items: center;
    border-left: 2px solid var(--sky-soft);
  }
  .ingredient:first-child { border-left: none; }
  .ingredient__art {
    width: 66px; height: 66px; border-radius: 50%;
    border: 3px solid var(--plum); background: var(--white);
    display: flex; align-items: center; justify-content: center;
  }
  .ingredient__art span { width: 44px; height: 44px; border-radius: 50%; display: block; }
  .ingredient__name {
    margin-top: 12px; color: var(--white); font-size: 11px; font-weight: 700;
    text-align: center; line-height: 1.1; text-transform: uppercase; min-height: 26px;
  }

  .flavour {
    position: absolute; left: 0; top: 955px; width: 100%; text-align: center;
    font-family: "Cormorant SC", serif; font-weight: 600; font-size: 44px;
    color: var(--plum); letter-spacing: 1px;
  }
</style>
</head>
<body>
  <main class="pack">
    <div class="pack__top"></div>
    <div class="pack__stripe"></div>

    <div class="brand"><span class="brand__name">Lumen<br>Fuel</span></div>

    <div class="title">
      <span class="title__line title__line--keto">KETO</span>
      <span class="title__line title__line--bar">BAR</span>
    </div>

    <ul class="claims">
      <li><svg width="18" height="18" viewBox="0 0 18 18"><circle cx="9" cy="9" r="7" fill="none" stroke="#fff" stroke-width="2"/><path d="M5 9l3 3 6-7" fill="none" stroke="var(--check)" stroke-width="2.4"/></svg>Suitable for a keto / LCHF diet,</li>
      <li><svg width="18" height="18" viewBox="0 0 18 18"><circle cx="9" cy="9" r="7" fill="none" stroke="#fff" stroke-width="2"/><path d="M5 9l3 3 6-7" fill="none" stroke="var(--check)" stroke-width="2.4"/></svg>3.5g net carbs,</li>
      <li><svg width="18" height="18" viewBox="0 0 18 18"><circle cx="9" cy="9" r="7" fill="none" stroke="#fff" stroke-width="2"/><path d="M5 9l3 3 6-7" fill="none" stroke="var(--check)" stroke-width="2.4"/></svg>Vegan</li>
    </ul>

    <svg class="wave" viewBox="0 0 560 440" preserveAspectRatio="none" aria-hidden="true">
      <path d="M0 40 C60 40 70 150 170 160 C280 170 300 120 380 200 C440 260 500 280 560 250 L560 440 L0 440 Z" fill="var(--sky-soft)"/>
      <path d="M0 70 C60 70 80 170 180 180 C290 190 320 150 390 230 C450 290 510 300 560 290 L560 440 L0 440 Z" fill="var(--paper)"/>
      <path d="M30 220 C40 200 60 195 90 195 L200 195 M360 195 L470 195 C500 195 520 205 525 240" fill="none" stroke="var(--plum)" stroke-width="2"/>
    </svg>

    <section class="ingredients">
      <span class="ingredients__label">INGREDIENTS</span>
      <div class="ingredients__band"></div>
      <ul class="ingredients__row">
        <li class="ingredient"><div class="ingredient__art"><span role="img" aria-label="Illustration of peanuts" style="background:#c98a55"></span></div><span class="ingredient__name">Peanuts</span></li>
        <li class="ingredient"><div class="ingredient__art"><span role="img" aria-label="Illustration of almonds" style="background:#b9794a"></span></div><span class="ingredient__name">Almonds</span></li>
        <li class="ingredient"><div class="ingredient__art"><span role="img" aria-label="Illustration of coconut" style="background:#a07550"></span></div><span class="ingredient__name">Coconut</span></li>
        <li class="ingredient"><div class="ingredient__art"><span role="img" aria-label="Illustration of pumpkin seeds" style="background:#d8c25a"></span></div><span class="ingredient__name">Pumpkin<br>seeds</span></li>
        <li class="ingredient"><div class="ingredient__art"><span role="img" aria-label="Illustration of chia seeds" style="background:#4a4a4e"></span></div><span class="ingredient__name">Chia</span></li>
        <li class="ingredient"><div class="ingredient__art"><span role="img" aria-label="Illustration of sunflower seeds" style="background:#8a8a86"></span></div><span class="ingredient__name">Sunflower<br>seeds</span></li>
      </ul>
    </section>

    <p class="flavour">Almond Flavour</p>
  </main>
</body>
</html>
```